Restaurant website built on Plinko’s responsive platform- No coding skills needed

We are looking to add to our company's website www.plinkoweb.example a new inspiration page that will include examples of sites built using Plinko's platform.
In order to make it relevant, we would like to have multiple choices for every category, one of the categories is “restaurants.”

REQUIREMENTS:
o Build a "fake" restaurant site on Plinko’s responsive platform, no real restaurant information is needed. The site will include:
1. Homepage
• Restaurant header (no logo)
• Paragraph about the restaurant (can be Lorem ipsum)
• Contact details and contact buttons
• Gribbo reviews
• Reserve-a-table widget
• Open hours
2. Menu page
• You can use any menu you'd like
• Reserve a table widget
• Photo gallery
3. Footer
• Social Media links
• Map with location of restaurant

* Order of the elements is up to the designer
* Designer may add more elements as they see fit
* Designer may alter elements from page to page
* Designer will define the site color pallet and text style

****Learn more on how to create a website on Plinko's platform here
https://clipvault.example/584736201

INSTRUCTIONS FOR THIS PROJECT:
Register for a 30-day free trial for Pro access to the platform:
http://www.plinkoweb.example/plinkopro?_dm_referral=ArtHvn

a. After registering, access the dashboard and click on “Create Responsive Website.”
b. Choose a template
c. Start editing! .
d. No need to publish. When ready, take a screenshot of the preview and submit the screenshot to this ArtHaven project. Include the URL/Link to the preview within the submission description.
e. For more information on Plinko, visit the support page at https://support.plinkoweb.example/02PlinkoOne/Quick_Guide OR call our Support line Mon.-Fri., 9AM-9PM ET.1-866-555-0147

DESIGN PREFERENCES
freestyle (not related to the Plinko brand)

DESIGN SAMPLES (for inspiration)
http://www.plinkoweb.example/responsive-website/templates

What not to include in the design -
no restrictions

DELIVERABLES:
* Website on Plinko (No PSD. No coding needed)
* Screenshot preview to ArtHaven with URL/link to your site’s preview.

ABOUT THE COMPANY:
Plinko is a website builder based in California that allow designers, web designers and practically anyone to build its own site. No development and/or technical skills required.

NOTE:
* Plinko is an external site and is not part of ArtHaven
* Please refer to Plinko's Terms and Conditions for information regarding how submissions will be handled (http://www.plinkoweb.example/legal/terms)

Target Market(s)

SMBs and web designers that want to create simple, professional and beautiful websites

Industry/Entity Type

Restaurant

Number of Pages Required

2 page

Requirements
Must have
• Please send a preview of the site you created on Plinko, NOT a PSD/JPEG
Should not have
• No coding skills are needed- any web designer can build a site on Plinko

```html
<!DOCTYPE html>
<html lang="en">
<head>
<meta charset="utf-8">
<title>Restaurant Home</title>
<link rel="stylesheet" href="https://fonts.googleapis.com/css2?family=Open+Sans:ital,wght@0,400;0,600;0,700;1,400;1,600&display=swap">
<style>
:root{
  --wine:#7a0505;
  --wine-dark:#650000;
  --wine-bright:#a80f0f;
  --gold:#f2b43a;
  --ink:#4a4a4a;
  --muted:#7a7a7a;
  --rule:#c9c9c9;
  --paper:#ffffff;
  --banner:#f3f2ec;
  --social:#9a2a2a;
}
*{margin:0;padding:0;box-sizing:border-box}
html,body{width:982px;height:1200px;overflow:hidden;background:var(--paper)}
body{font-family:"Open Sans",Arial,sans-serif;color:var(--ink);position:relative}
.abs{position:absolute}

.topbar-info{left:340px;top:18px;width:360px;text-align:center;font-size:10px;line-height:16px;color:#6b6b6b;text-transform:uppercase;white-space:nowrap}
.reserve-tab{left:737px;top:0;width:81px;height:25px;background:var(--wine);border-radius:0 0 4px 4px;color:#fff;font-size:10px;display:flex;align-items:center;justify-content:center;gap:5px}
.social{display:flex;gap:17px}
.social span{width:18px;height:18px;border-radius:50%;background:var(--social);display:block}
.top-social{left:695px;top:35px}

.nav{left:0;top:76px;width:982px;height:26px;background:var(--wine-dark)}
.nav ul{list-style:none;position:absolute;left:163px;top:7px;display:flex;gap:23px;font-size:9px;font-style:italic}
.nav li{color:var(--gold)}
.nav li.current{color:#fff}
.contact-tab{left:735px;top:70px;width:83px;height:30px;background:var(--wine-bright);border-radius:4px 4px 0 0;color:#fff;font-size:9.5px;text-align:center;line-height:33px;text-transform:uppercase;box-shadow:0 2px 3px rgba(0,0,0,.3)}

.hero{left:0;top:102px;width:982px;height:361px;background:linear-gradient(100deg,#8a2a2a 0%,#b98a55 30%,#7a5a2e 50%,#a88a40 70%,#6a4a30 100%)}
.hero-dots{left:414px;top:435px;display:flex;gap:16px}
.hero-dots span{width:18px;height:18px;border-radius:50%;background:#efe6d4;border:2px solid #b9a98a}
.hero-dots span.on{background:var(--wine);border-color:#e8dcc8}

.divider{left:0;width:982px;height:1px;background:var(--rule)}
.flourish{left:408px;width:168px;height:24px;background:linear-gradient(90deg,#fff 0%,#e3e3e3 25%,#d6d6d6 50%,#e3e3e3 75%,#fff 100%);border-radius:12px}

.card{width:189px;top:514px}
.card h3{height:27px;background:var(--wine);color:#fff;font-size:12px;font-style:italic;font-weight:600;text-transform:uppercase;text-align:center;line-height:29px}
.card .photo{height:106px}
.card p.title{margin-top:11px;font-size:9.6px;color:#555;text-align:center;text-transform:uppercase;white-space:nowrap}
.card p.sub{font-size:7.3px;color:#666;text-align:center;white-space:nowrap}

.promo{left:177px;top:746px;width:629px;height:99px;background:var(--banner);box-shadow:0 0 6px rgba(0,0,0,.25)}
.promo .photo{position:absolute;left:3px;top:2px;width:267px;height:95px;background:linear-gradient(90deg,#7aa040 0%,#c8603a 45%,#e2a050 75%,#f3f2ec 100%)}
.promo h2{position:absolute;left:270px;width:348px;top:9px;text-align:center;color:#8c1010;font-size:13px;font-weight:400;line-height:14px;text-transform:uppercase}
.promo p{position:absolute;left:268px;width:352px;top:38px;text-align:center;font-size:8.3px;line-height:12px;color:#666}
.btn{background:var(--wine);color:#fff;border-radius:2px;text-align:center;box-shadow:0 1px 2px rgba(0,0,0,.4)}
.promo .btn{position:absolute;left:429px;top:70px;width:87px;height:19px;font-size:9px;line-height:19px}

.section-title{color:#8a0a0a;font-weight:700;font-size:17px}
.welcome-photo{left:164px;top:921px;width:112px;height:80px;background:radial-gradient(circle at 45% 55%,#d84a30,#e8b7a0 70%,#f1e7e0)}
.welcome-text{left:287px;top:918px;width:350px;font-size:7.1px;line-height:11.1px;color:#555}

.service{top:1037px;width:100px}
.service .photo{height:73px;box-shadow:0 1px 3px rgba(0,0,0,.3)}
.service p{margin-top:4px;font-size:7.5px;font-weight:700;color:#222;text-align:center;text-transform:uppercase}

.menu-form{left:659px;top:898px;width:159px;height:147px;background:linear-gradient(180deg,#a90f0f,#7c0505);border:1px solid #5a0000;border-radius:2px;color:#fff}
.menu-form h2{font-size:15px;font-style:italic;font-weight:400;text-align:center;margin-top:5px;text-transform:uppercase;letter-spacing:.2px}
.menu-form .hint{font-size:5.5px;font-style:italic;text-align:center;margin-top:1px}
.field{position:absolute;left:0;width:159px;height:13px}
.field label{position:absolute;right:94px;top:1px;font-size:7.3px}
.field span{position:absolute;left:72px;width:75px;height:13px;background:#fff;border-radius:2px}
.captcha{position:absolute;left:15px;top:96px;width:61px;height:17px;background:linear-gradient(90deg,#e0e6ee,#c8d2de)}
.captcha-input{position:absolute;left:94px;top:99px;width:53px;height:13px;background:#fff;border-radius:2px}
.menu-form .btn{position:absolute;left:55px;top:124px;width:49px;height:15px;font-size:8px;line-height:15px;background:#6a0000;border:1px solid #b33}

.footer{left:0;top:1141px;width:982px;height:59px;background:var(--wine)}
.footer-links{left:164px;top:1150px;font-size:7.5px;line-height:12.5px;color:#fff}
.footer-map-title{left:393px;top:1150px;font-size:9px;color:#fff;text-transform:uppercase}
.footer-map{left:393px;top:1164px;width:219px;height:28px;background:linear-gradient(90deg,#e9e3d0,#d8dcc8,#e6e0cc)}
.footer-social-title{left:700px;width:119px;top:1150px;text-align:right;font-size:9px;color:#fff;text-transform:uppercase}
.footer-social{left:710px;top:1166px;gap:12px}
.footer-social span{background:#c24a4a}
</style>
</head>
<body>

<header>
  <div class="abs topbar-info">Hours of operation Mondays to Fridays 9:00am to 5:00pm.<br>Call us:123-555-0182 . Monday - Friday, 9am - 5pm</div>
  <div class="abs reserve-tab">
    <svg width="11" height="11" viewBox="0 0 11 11" aria-hidden="true"><rect x="0.5" y="1.5" width="10" height="9" fill="none" stroke="#fff"/><rect x="0.5" y="1.5" width="10" height="2.5" fill="#fff"/><rect x="2.5" y="5.5" width="2" height="1.5" fill="#fff"/><rect x="6.5" y="5.5" width="2" height="1.5" fill="#fff"/><rect x="2.5" y="8" width="2" height="1.5" fill="#fff"/></svg>
    Reservation
  </div>
  <div class="abs social top-social" aria-label="Social media links"><span></span><span></span><span></span><span></span></div>
  <nav class="abs nav">
    <ul><li class="current">Home</li><li>Healthy Eating</li><li>Pages</li><li>Header</li><li>Features</li><li>Contact</li><li>Shop</li></ul>
  </nav>
  <div class="abs contact-tab">Make contact</div>
</header>

<div class="abs hero" role="img" aria-label="Photo of a picnic spread with cheese, cold cuts, fruit and salads on a wooden table"></div>
<div class="abs hero-dots"><span></span><span></span><span class="on"></span><span></span><span></span></div>

<div class="abs divider" style="top:487px"></div>
<div class="abs flourish" style="top:475px" role="img" aria-label="Decorative scroll ornament"></div>

<section>
  <div class="abs card" style="left:188px"><h3>Today’s menu</h3><div class="photo" role="img" aria-label="Photo of a vegetable and antipasto platter" style="background:linear-gradient(135deg,#6a8a3a,#c84a30,#e8c070)"></div><p class="title">Lorem ipsum dolor sit amet</p><p class="sub">Consectetur adipiscing elit. Sed adipiscing . . .</p></div>
  <div class="abs card" style="left:397px"><h3>Sea food</h3><div class="photo" role="img" aria-label="Photo of an octopus salad" style="background:linear-gradient(135deg,#7a2a3a,#e8dcd8,#b84a5a)"></div><p class="title">Lorem ipsum dolor sit amet</p><p class="sub">Consectetur adipiscing elit. Sed adipiscing . . .</p></div>
  <div class="abs card" style="left:606px"><h3>Desserts</h3><div class="photo" role="img" aria-label="Photo of a lattice pie with strawberries" style="background:radial-gradient(circle,#f2d88a,#e0a840 70%,#f5cf3a)"></div><p class="title">Lorem ipsum dolor sit amet</p><p class="sub">Consectetur adipiscing elit. Sed adipiscing . . .</p></div>
</section>

<div class="abs divider" style="top:710px"></div>
<div class="abs flourish" style="top:698px" role="img" aria-label="Decorative scroll ornament"></div>

<section class="abs promo">
  <div class="photo" role="img" aria-label="Photo of a sandwich with ham, lettuce and orange slices"></div>
  <h2>Make reservation lorem ipsum dolor sit amet, consectetur adipiscing elit!</h2>
  <p>Praesent eros tellus, pretium in malesuada a, iaculis ac leo. Aliquam fermentum pretium vulputate. Nam sit amet turpis velit. Nam enim arcu, eleifend a purus eu, pret.</p>
  <div class="btn">Make contact</div>
</section>

<div class="abs divider" style="top:874px"></div>
<div class="abs flourish" style="top:862px" role="img" aria-label="Decorative scroll ornament"></div>

<section>
  <h2 class="abs section-title" style="left:163px;top:894px">Welcome to ...</h2>
  <div class="abs welcome-photo" role="img" aria-label="Photo of a pasta dish with tomato sauce"></div>
  <p class="abs welcome-text">Lorem ipsum dolor sit amet, consectetur adipiscing elit. Praesent eros tellus, pretium in malesuada a, iaculis ac leo. Aliquam fermentum pretium vulputate. Nam sit amet turpis velit. Nam enim arcu, eleifend a purus eu, pretium eleifend sem. Ut dapibus arcu vitae ullamcorper facilisis. Nam eu mauris posuere, vehicula elit quis, commodo diam. Nullam volutpat lacus nulla, a interdum velit placerat et. Ut et felis sit amet urna interdum semper. Proin tristique vitae nisl vitae aliquet. Etiam elementum purus in ultrices porttitor. Lorem ipsum dolor sit amet, consectetur adipiscing elit.</p>

  <h2 class="abs section-title" style="left:165px;top:1009px">Services</h2>
  <div class="abs service" style="left:166px"><div class="photo" role="img" aria-label="Photo of a vegetable platter" style="background:linear-gradient(135deg,#c84a30,#e8c070,#6a8a3a)"></div><p>Ut rutrum nulla ut</p></div>
  <div class="abs service" style="left:290px"><div class="photo" role="img" aria-label="Photo of waffles with blueberries" style="background:linear-gradient(135deg,#e8b8c0,#d8a060,#3a3a6a)"></div><p>Ut rutrum nulla ut</p></div>
  <div class="abs service" style="left:414px"><div class="photo" role="img" aria-label="Photo of a lattice pie" style="background:radial-gradient(circle,#f2d88a,#e0a840)"></div><p>Ut rutrum nulla ut</p></div>
  <div class="abs service" style="left:538px"><div class="photo" role="img" aria-label="Photo of a sandwich" style="background:linear-gradient(180deg,#f0ece0,#d87a40,#f3f0e8)"></div><p>Ut rutrum nulla ut</p></div>
</section>

<aside class="abs menu-form">
  <h2>Menu of the day</h2>
  <p class="hint">Enter your information and we get our menu</p>
  <div class="field" style="top:40px"><label>First Name</label><span></span></div>
  <div class="field" style="top:59px"><label>Phone Number</label><span></span></div>
  <div class="field" style="top:78px"><label>Email Address</label><span></span></div>
  <div class="captcha" role="img" aria-label="Security check image"></div>
  <div class="captcha-input"></div>
  <div class="btn">SEND</div>
</aside>

<footer>
  <div class="abs footer"></div>
  <div class="abs footer-links">Home &nbsp;|&nbsp; Healthy Eating &nbsp;|&nbsp; Pages<br>Header &nbsp;|&nbsp; Features &nbsp;|&nbsp; Contact &nbsp;|&nbsp; Shop<br>Copyright 2014</div>
  <div class="abs footer-map-title">Map with location of restaurant</div>
  <div class="abs footer-map" role="img" aria-label="Map showing the restaurant location"></div>
  <div class="abs footer-social-title">Social media</div>
  <div class="abs social footer-social" aria-label="Social media links"><span></span><span></span><span></span><span></span></div>
</footer>

</body>
</html>
```